Criação de Folder para Logística, Entrega & Armazenamento
" Na grande maioria dos meus negocio, hoje estamos com foco na venda de Gesso Agrícola, Calcário e milho. fazemos negócios com Produtores rurais e granjas. vendemos o gesso e entregamos com a nossa frota de caminhões seja, frota própria ou caminhões agregado. da mesma maneira são os negócios com grãos, originamos os grãos dos produtores e vedemos para as granjas, entregamos com a nossa frota própria ou caminhões agregados. "

```html
<!DOCTYPE html>
<html lang="pt-BR">
<head>
<meta charset="UTF-8">
<title>Terra Viva – Folder</title>
<link rel="stylesheet" href="https://fonts.googleapis.com/css2?family=Dancing+Script:wght@500&family=Open+Sans:wght@400;800&display=swap">
<style>
  :root {
    --page-bg: #ececec;
    --paper: #ffffff;
    --orange-dark: #c2701f;
    --orange: #d98b34;
    --brown: #5a3413;
    --brown-text: #8a5522;
    --green: #3d8a2c;
    --wheat-1: #efe3c8;
    --wheat-2: #d7b67a;
    --wheat-3: #b9925a;
  }
  * { box-sizing: border-box; margin: 0; padding: 0; }
  html, body { width: 1200px; height: 1200px; overflow: hidden; }
  body { background: var(--page-bg); position: relative; font-family: "Open Sans", sans-serif; }

  .cover {
    position: absolute; left: 200px; top: 50px;
    width: 800px; height: 1100px;
    background: var(--paper);
    box-shadow: 0 6px 24px rgba(0,0,0,.12);
    overflow: hidden;
  }
  .cover__header { position: absolute; left: 0; top: 0; width: 800px; height: 110px; }

  .brand-name {
    position: absolute; top: 126px; left: 0; width: 100%;
    text-align: center;
    font-size: 50px; font-weight: 400; line-height: 1.2;
    color: var(--brown-text); letter-spacing: .5px;
  }

  .cover__photo {
    position: absolute; left: 40px; top: 215px; width: 720px; height: 380px;
    background:
      radial-gradient(ellipse at 45% 45%, var(--wheat-2) 0%, var(--wheat-3) 25%, var(--wheat-1) 60%, rgba(255,255,255,0) 80%);
    opacity: .9;
  }

  .tagline {
    position: absolute; top: 600px; left: 0; width: 100%;
    text-align: center; font-family: "Dancing Script", cursive;
    font-size: 62px; line-height: 1.25; color: var(--green); font-weight: 500;
  }
  .tagline__rule {
    position: absolute; top: 800px; left: 200px; width: 400px; height: 2px;
    background: var(--green);
  }
  .tagline__dots {
    position: absolute; top: 792px; left: 360px; width: 80px; height: 4px;
    border-top: 4px dotted var(--green);
  }

  .cover__footer { position: absolute; left: 0; top: 950px; width: 800px; height: 130px; }
  .slogan {
    position: absolute; top: 969px; left: 0; width: 720px;
    text-align: center; font-size: 31px; font-weight: 800; line-height: 1.2;
    color: var(--brown); letter-spacing: .5px;
  }
</style>
</head>
<body>
  <main class="cover">
    <svg class="cover__header" viewBox="0 0 800 110" aria-hidden="true">
      <defs>
        <linearGradient id="bandGrad" x1="0" x2="1" y1="0" y2="0">
          <stop offset="0" stop-color="#e0a25a"/>
          <stop offset=".5" stop-color="#cf7f2c"/>
          <stop offset="1" stop-color="#c2701f"/>
        </linearGradient>
      </defs>
      <path d="M0 0 H800 V68 H0 Z" fill="url(#bandGrad)"/>
      <path d="M0 76 H800 V92 H0 Z" fill="var(--brown)"/>
      <path d="M0 92 H800 V98 H0 Z" fill="var(--orange)"/>
    </svg>

    <p class="brand-name">Terra Viva</p>

    <div class="cover__photo" role="img" aria-label="Fotografia de espigas de trigo douradas em campo, com bordas esmaecidas"></div>

    <h1 class="tagline">O que há de melhor em<br>grãos e fertilizantes</h1>
    <div class="tagline__rule"></div>
    <div class="tagline__dots"></div>

    <svg class="cover__footer" viewBox="0 0 800 130" aria-hidden="true">
      <defs>
        <linearGradient id="ribbonGrad" x1="0" x2="1" y1="0" y2="0">
          <stop offset="0" stop-color="#f3c98c"/>
          <stop offset=".6" stop-color="#e09a48"/>
          <stop offset="1" stop-color="#c97522"/>
        </linearGradient>
      </defs>
      <path d="M0 0 H680 Q720 0 720 38 Q720 76 680 76 H0 Z" fill="url(#ribbonGrad)"/>
      <path d="M0 86 H800 V104 H0 Z" fill="var(--brown)"/>
      <path d="M0 110 H800 V116 H0 Z" fill="var(--orange)"/>
    </svg>
    <p class="slogan">VENDEMOS E LEVAMOS ATÉ VOCÊ!</p>
  </main>
</body>
</html>
```